MENSTRUATION

Website Design Brief
*Note: I am also a professional graphic designer, so please make a note of that and present your best work. If you are not a professional graphic designer, please do not post anything or invest time.
Project Title: Cyclewise Website for Teens and Parents
________________________________________
1. Project Overview
We aim to create an engaging, educational, and supportive online platform dedicated to menstruation awareness and guidance.
The website will serve two primary audiences:
1. Teens aged 13–16
o Objective: Educate and empower them with knowledge about menstruation, menstrual health, hygiene, and emotional well-being.
o Tone: Playful, approachable, friendly, and relatable.
2. Parents/Women
o Objective: Provide in-depth resources, support communities, and expert advice to help them support their teens (or themselves) through menstruation-related challenges.
o Tone: Serious, mature, trustworthy, and empathetic.
The website will be dual-themed to cater to each audience’s emotional and visual expectations while maintaining a unified brand identity.
2. Goals & Objectives
• Educate teens in a fun and approachable way about menstruation.
• Provide safe spaces for open discussion, both for teens and for parents.
• Encourage intergenerational conversation between parents and teens.
• Destigmatize menstruation through positive, engaging design and language.
• Offer credible information backed by health professionals.
3. Target Audiences
• Primary Teen Audience (13–16 years old):
o Tech-savvy, visually driven, short attention spans.
o Need reassurance, relatability, and accurate information.
• Primary Parent/Women Audience:
o Concerned with their children’s well-being.
o Seeking practical advice, medical information, and a supportive community.
4. Website Structure & Sections
A. Teen Section ("Playful & Cute Look")
• Design Style:
o Bright pastel colors (pink, lavender, sky blue, mint).
o Whimsical illustrations (Lumvic/Korrin-like characters, friendly mascots).
o Sparkles, soft shapes, rounded edges, playful animations.
• Features:
o Educational Guides – Menstrual cycle basics, hygiene tips, dealing with cramps, myths & facts.
o Interactive Period Tracker – Cute UI, gamified elements.
o Ask an Expert – Anonymous Q&A with professionals.
o Story Corner – Real teen stories about first periods.
o Fun Zone – Quizzes, mood trackers, self-care tips.
B. Parent/Women Section ("Serious & Mature Look")
• Design Style:
o Neutral and warm tones (earthy beige, soft gray, deep burgundy).
o Clean layouts, minimalistic icons, serif fonts for elegance.
o Subtle animations for professionalism.
• Features:
o Expert Articles – Menstrual health, nutrition, emotional support.
o Parenting Tips – Helping teens manage periods with confidence.
o Discussion Forum – Moderated safe space for parents/women to share experiences.
o Medical Resources – Links to reputable health organizations.
o Downloadable Guides – Printable resources for home use.
C. Shared/Bridging Content (Unified Brand Tone)
• About Us – Mission, vision, credibility.
• Health Professional Endorsements – Bios of medical advisors.
• Contact & Support – Email, live chat, helpdesk.
• Language Toggle – Option for multiple languages.
• Accessibility Features – Dyslexia-friendly fonts, text resizing, high contrast mode.
5. Navigation
• Dual-Entry Landing Page
o Upon visiting, users choose: "For Teens" or "For Parents/Women".
o Each section retains its design style but keeps consistent logo and branding.
6. Technical Requirements
• Responsive Design – Works seamlessly on mobile, tablet, and desktop.
• Secure Login – For community areas (with parental consent for minors).
• Moderation Tools – AI-assisted and human moderation to ensure safety.
• SEO Optimization – For health-related keyword ranking.
• CMS – Easy content updates for articles and resources.
7. Additional Creative Ideas
• Mascot Character – A friendly animated character guiding teens through content.
• Parent-Teen Joint Activities Section – Fun bonding ideas related to menstrual health education.
• Myth-Busting Series – Quick animated videos addressing common menstrual myths.
• Interactive Body Map – Clickable diagram explaining reproductive anatomy in a simple way.
• Monthly Newsletter – Separate teen and parent editions.
• Private Journaling Feature – Teens can log moods, symptoms, and notes.
8. Brand Personality
• For Teens: Friendly, encouraging, sparkly, non-judgmental, empowering.
• For Parents: Respectful, informative, empathetic, trustworthy.
9. Deliverables Expected from Designers
• Wireframes for both sections.
• Complete UI/UX design with separate visual themes for each audience.
• Branding package (color palettes, typography, illustration style).
• Icons & graphics consistent with each section’s theme.
• Guidelines for animations and transitions.
For the teens section something Lumvic-like or Korrin-like could also be interesting.
Please note that I am a professional graphic designer so please only spend time doing a design that you
truly feel is awesome and professional, otherwise it will just be a waste of time. Doing drafts with chatgpt will not work, I've seen them all.
thanks
1 page

```html
<!DOCTYPE html>
<html lang="en">
<head>
<meta charset="utf-8">
<title>Cyclewise</title>
<link href="https://fonts.googleapis.com/css2?family=Poppins:wght@300;400;500;600;700;800&display=swap" rel="stylesheet">
<style>
:root{
  --board:#f7aac8;
  --lavender:#efeafb;
  --pink:#f6a3bf;
  --pink-soft:#fbc7d8;
  --purple-deep:#6b4fb5;
  --ink:#1f1d24;
  --muted:#5c5864;
  --white:#ffffff;
  --cream:#fff6ef;
  --footer:#222126;
  --line:#e4dff0;
}
*{box-sizing:border-box;margin:0;padding:0}
html,body{width:1200px;height:4930px;overflow:hidden}
body{background:var(--board);font-family:"Poppins",sans-serif;color:var(--ink);position:relative}
.abs{position:absolute}
.photo{position:absolute;border-radius:10px}
.brand-name{font-family:"Poppins",sans-serif;font-weight:700;font-size:24px;color:var(--ink);line-height:1;display:flex;align-items:center;gap:10px}
.brand-dot{width:14px;height:14px;border-radius:50%;background:var(--pink)}
.btn{position:absolute;display:flex;align-items:center;justify-content:center;border-radius:6px;font-weight:600;font-size:11px;color:var(--ink);background:var(--pink)}

.landing{left:90px;top:90px;width:1020px;height:720px;background:var(--lavender)}
.landing .brand{left:0;width:1020px;top:48px;display:flex;justify-content:center}
.choice{font-size:18px;height:53px;width:207px;background:#f8a6c4;border-radius:6px}

.teen{left:90px;top:871px;width:1020px;height:3997px;background:var(--white)}
.teen-head{left:0;top:0;width:1020px;height:300px;background:linear-gradient(#efeafb,#fff)}
.nav{display:flex;align-items:center;font-size:10px;font-weight:600;text-transform:uppercase}
.hero-disc{left:228px;top:1040px;width:390px;height:390px;border-radius:50%;background:radial-gradient(circle at 40% 35%,rgba(190,160,235,.92),rgba(140,105,200,.92));border:8px solid rgba(220,200,250,.55);display:flex;flex-direction:column;align-items:center;justify-content:center;text-align:center;color:#fff}
.hero-disc h1{font-size:44px;line-height:1.02;font-weight:300}
.hero-disc h1 b{font-weight:800}
.hero-disc p{font-size:15px;margin-top:14px;line-height:1.35}
.section-title{position:absolute;left:0;width:1200px;text-align:center;font-size:29px;font-weight:400}
.section-title b{font-weight:800}
.guide{position:absolute;top:1590px;width:224px;height:295px;background:var(--lavender);border-radius:8px;padding:16px}
.guide .img{height:166px;border-radius:6px}
.guide h3{font-size:11px;font-weight:600;margin-top:20px;text-transform:uppercase}
.guide p{font-size:9px;color:var(--muted);margin-top:10px;line-height:1.45;width:170px}
.arrow{position:absolute;right:14px;bottom:14px}
.track{left:136px;top:2027px;width:928px;height:490px;background:linear-gradient(90deg,#e8d3e7,#f1e2ee);border-radius:6px;overflow:hidden}
.track h2{font-size:34px;line-height:1.05;font-weight:400;white-space:nowrap}
.track h2 b{font-weight:800}
.track p{font-size:12px;color:var(--muted);line-height:1.6;margin-top:18px}
.checks{list-style:none;margin-top:14px}
.checks li{display:flex;align-items:center;gap:10px;font-size:11.5px;font-weight:600;margin-top:12px}
.story{position:absolute;top:2659px;width:295px;height:379px;background:var(--cream);border-radius:8px;padding:15px;border:1px solid #f8e6dc}
.story .img{height:207px;border-radius:6px}
.tag{display:inline-block;margin-top:14px;background:var(--pink);font-size:8px;font-weight:700;padding:2px 8px;border-radius:3px}
.story h3{font-size:11px;font-weight:700;margin-top:10px;line-height:1.4;text-transform:uppercase}
.story p{font-size:9.5px;color:var(--muted);margin-top:8px;line-height:1.45}
.ask{left:90px;top:3191px;width:1020px;height:580px;background:linear-gradient(180deg,#e8dbf8,#efe3fb 60%,#e6d6f6)}
.faq{left:201px;top:3344px;width:798px;height:331px;background:#fff;display:grid;grid-template-columns:1fr 1fr;grid-template-rows:1fr 1fr}
.faq div{padding:26px 24px 0 66px;position:relative;border-right:1px solid var(--line);border-bottom:1px solid var(--line)}
.faq svg{position:absolute;left:24px;top:26px}
.faq h4{font-size:11px;font-weight:700}
.faq p{font-size:9.5px;color:var(--muted);margin-top:8px;line-height:1.6}
.fun{left:136px;top:3857px;width:928px;height:488px;border-radius:8px;background:linear-gradient(120deg,#f3c7ee,#e9a6e8 55%,#f2b6ee);overflow:hidden}
.fun h2{font-size:35px;font-weight:400}
.fun h2 b{font-weight:700}
.tile{position:absolute;top:4096px;width:142px;height:157px;background:#fff;border-radius:4px;text-align:center;padding-top:16px}
.tile .ico{width:70px;height:62px;margin:0 auto;border-radius:50%}
.tile h4{font-size:12px;font-weight:500;margin-top:12px}
.tile p{font-size:8.5px;color:var(--muted);line-height:1.4;margin-top:6px}
.footer{left:90px;top:4437px;width:1020px;height:431px;background:var(--footer);color:#fff}
.round{position:absolute;width:40px;height:40px;border-radius:50%;background:var(--pink-soft);display:flex;align-items:center;justify-content:center}
</style>
</head>
<body>

<section class="abs landing">
  <div class="abs brand"><div class="brand-name" style="font-size:26px"><span class="brand-dot"></span>Cyclewise</div></div>
  <div class="photo" role="img" aria-label="Teen girl smiling outdoors in striped shirt" style="left:46px;top:124px;width:455px;height:490px;background:linear-gradient(135deg,#b8a35a,#6f8a3c 45%,#c9a2c4)"></div>
  <div class="photo" role="img" aria-label="Mother and daughter talking on a sofa" style="left:519px;top:124px;width:453px;height:490px;background:linear-gradient(135deg,#e4ddd6,#9c7c6a 50%,#6f7b8e)"></div>
  <div class="btn choice" style="left:170px;top:341px">For Teens</div>
  <div class="btn choice" style="left:639px;top:341px;background:#d7c3f6">For Parents</div>
  <div class="photo" role="img" aria-label="Fashion doll mascot" style="left:450px;top:561px;width:111px;height:159px;background:linear-gradient(#f0d59b,#e6b79a 40%,#d85aa4)"></div>
</section>

<section class="abs teen"><div class="abs teen-head"></div></section>

<div class="abs" style="left:134px;top:912px"><div class="brand-name"><span class="brand-dot"></span>Cyclewise</div></div>
<nav class="abs nav" style="left:584px;top:907px;height:20px">
  <span style="color:var(--pink)">For Teens</span>
  <span style="margin-left:28px">For Parents</span>
  <span style="margin-left:28px">Contact</span>
</nav>
<div class="btn" style="left:833px;top:900px;width:82px;height:30px;background:#fff;border:2px solid var(--ink);font-size:10px">Login</div>
<div class="btn" style="left:921px;top:900px;width:86px;height:30px;font-size:10px">Sign Up</div>
<div class="abs nav" style="left:1028px;top:907px;height:16px">ENG
  <svg width="10" height="8" style="margin-left:5px"><path d="M1 2l4 4 4-4" stroke="#1f1d24" fill="none" stroke-width="1.3"/></svg></div>
<div class="abs" style="left:584px;top:946px;width:480px;height:1px;background:var(--line)"></div>
<div class="abs" style="left:584px;top:945px;width:50px;height:3px;background:var(--pink);border-radius:2px"></div>

<div class="photo" role="img" aria-label="Teen girl breathing in the sunlight" style="left:136px;top:982px;width:928px;height:490px;background:linear-gradient(110deg,#a28a3c,#5f7b33 40%,#b89c73 65%,#9b93c0)"></div>
<div class="abs hero-disc">
  <h1><b>Your Body,</b><br>Your Journey<br><b>Let’s Make</b><br>It Fun!</h1>
  <p>Learn, track, and feel your<br>best—together.</p>
  <div class="btn" style="position:static;margin-top:22px;width:156px;height:33px;font-size:11px">Start Your Tracker</div>
</div>

<h2 class="section-title" style="top:1515px"><b>Educational</b> Guides</h2>
<article class="guide" style="left:136px"><div class="img" role="img" aria-label="Calendar marked with cycle days" style="background:linear-gradient(135deg,#d9cfd8,#b7a7b3)"></div><h3>Menstrual Cycle 101</h3><p>Lorem ipsum dolor sit amet, consectetur adipiscing elit, sed do eiusmod tempor incididunt</p><svg class="arrow" width="14" height="10"><path d="M0 5h12M8 1l4 4-4 4" stroke="#1f1d24" fill="none" stroke-width="1.3"/></svg></article>
<article class="guide" style="left:371px"><div class="img" role="img" aria-label="Hands holding a blue pad" style="background:linear-gradient(135deg,#9fb6d8,#6f8fc6)"></div><h3>Hygiene Tips</h3><p>Lorem ipsum dolor sit amet, consectetur adipiscing elit, sed do eiusmod tempor incididunt</p><svg class="arrow" width="14" height="10"><path d="M0 5h12M8 1l4 4-4 4" stroke="#1f1d24" fill="none" stroke-width="1.3"/></svg></article>
<article class="guide" style="left:605px"><div class="img" role="img" aria-label="Hot water bottle held against the belly" style="background:linear-gradient(135deg,#e8d8d0,#8a7cc8)"></div><h3>Cramps &amp; Comfort</h3><p>Lorem ipsum dolor sit amet, consectetur adipiscing elit, sed do eiusmod tempor incididunt</p><svg class="arrow" width="14" height="10"><path d="M0 5h12M8 1l4 4-4 4" stroke="#1f1d24" fill="none" stroke-width="1.3"/></svg></article>
<article class="guide" style="left:838px"><div class="img" role="img" aria-label="Fact versus myth graphic" style="background:linear-gradient(#fbd2bd,#f8c4a8)"></div><h3>Myths vs Facts</h3><p>Lorem ipsum dolor sit amet, consectetur adipiscing elit, sed do eiusmod tempor incididunt</p><svg class="arrow" width="14" height="10"><path d="M0 5h12M8 1l4 4-4 4" stroke="#1f1d24" fill="none" stroke-width="1.3"/></svg></article>
<div class="btn" style="left:528px;top:1929px;width:144px;height:33px">Read All Guides</div>

<section class="abs track">
  <div class="photo" role="img" aria-label="Girl hugging herself in a pink knit sweater" style="left:0;top:0;width:520px;height:490px;border-radius:0;background:linear-gradient(90deg,#d9c3d8,#d6a6c8 50%,rgba(232,211,231,0))"></div>
  <div class="abs" style="left:536px;top:58px;width:350px">
    <h2><b>Track Your</b><br>Cycle, Earn Badges,<br><b>Feel Great!</b></h2>
    <p>Log your days, moods, and symptoms in a safe, private, and super-cute tracker. Sed ut perspiciatis unde omnis iste natus error sit voluptatem accusantium doloremque laudantium, totam rem aperiam, eaque ipsa quae ab illo inventore veritatis et quasi architecto</p>
    <ul class="checks">
      <li><svg width="13" height="13"><circle cx="6.5" cy="6.5" r="6.5" fill="#6b4fb5"/><path d="M3.5 6.8l2 2 4-4" stroke="#fff" fill="none" stroke-width="1.5"/></svg>Lorem ipsum dolor sit amet, consectetur adipiscing</li>
      <li><svg width="13" height="13"><circle cx="6.5" cy="6.5" r="6.5" fill="#6b4fb5"/><path d="M3.5 6.8l2 2 4-4" stroke="#fff" fill="none" stroke-width="1.5"/></svg>Aenean ornare tortor eu volutpat ullamcorper.</li>
      <li><svg width="13" height="13"><circle cx="6.5" cy="6.5" r="6.5" fill="#6b4fb5"/><path d="M3.5 6.8l2 2 4-4" stroke="#fff" fill="none" stroke-width="1.5"/></svg>Mauris a sem luctus, luctus lacus non, posuere</li>
    </ul>
    <div class="btn" style="position:static;margin-top:22px;width:142px;height:33px;background:#b79ef0">Start Tracking</div>
  </div>
</section>

<h2 class="section-title" style="top:2586px"><b>Real Stories from</b> Real Teens</h2>
<article class="story" style="left:136px"><div class="img" role="img" aria-label="Portrait of a smiling teen in a park" style="background:linear-gradient(135deg,#6f8a46,#3f5a2a)"></div><span class="tag">4 June 2025</span><h3>Curabitur ac elit mollis, commodo dui vitae, venenatis enim.</h3><p>Lorem ipsum dolor sit amet, consectetur adipiscing elit, sed do eiusmod tempor incididunt ut labore et dolore magna aliqua. Ut enim ad minim</p><svg class="arrow" width="14" height="10"><path d="M0 5h12M8 1l4 4-4 4" stroke="#1f1d24" fill="none" stroke-width="1.3"/></svg></article>
<article class="story" style="left:452px"><div class="img" role="img" aria-label="Portrait of a laughing teen in sunlight" style="background:linear-gradient(135deg,#c69a4a,#5e6a3a)"></div><span class="tag">4 June 2025</span><h3>Curabitur ac elit mollis, commodo dui vitae, venenatis enim.</h3><p>Lorem ipsum dolor sit amet, consectetur adipiscing elit, sed do eiusmod tempor incididunt ut labore et dolore magna aliqua. Ut enim ad minim</p><svg class="arrow" width="14" height="10"><path d="M0 5h12M8 1l4 4-4 4" stroke="#1f1d24" fill="none" stroke-width="1.3"/></svg></article>
<article class="story" style="left:767px"><div class="img" role="img" aria-label="Teen sitting on a sofa at home" style="background:linear-gradient(135deg,#d9d7d2,#8fa0a8)"></div><span class="tag">4 June 2025</span><h3>Curabitur ac elit mollis, commodo dui vitae, venenatis enim.</h3><p>Lorem ipsum dolor sit amet, consectetur adipiscing elit, sed do eiusmod tempor incididunt ut labore et dolore magna aliqua. Ut enim ad minim</p><svg class="arrow" width="14" height="10"><path d="M0 5h12M8 1l4 4-4 4" stroke="#1f1d24" fill="none" stroke-width="1.3"/></svg></article>
<div class="btn" style="left:526px;top:3084px;width:150px;height:32px">Share Your Story</div>

<section class="abs ask"></section>
<h2 class="section-title" style="top:3258px"><b>Ask Us Anything –</b> It’s Anonymous!</h2>
<div class="abs faq">
  <div><svg width="22" height="22"><circle cx="11" cy="11" r="11" fill="#6b4fb5"/><path d="M6.5 11.3l3 3 6-6" stroke="#fff" fill="none" stroke-width="1.8"/></svg><h4>Dolorem eum fugiat quo voluptas nulla pariatur?</h4><p>Sed ut perspiciatis unde omnis iste natus error sit voluptatem accusantium doloremque laudantium, totam rem aperiam, eaque ipsa quae ab illo inventore veritatis et quasi architecto beatae vitae dicta sunt explicabo. Nemo enim ipsam voluptatem quia voluptas sit aspernatur aut odit aut</p></div>
  <div style="border-right:0"><svg width="22" height="22"><circle cx="11" cy="11" r="11" fill="#6b4fb5"/><path d="M6.5 11.3l3 3 6-6" stroke="#fff" fill="none" stroke-width="1.8"/></svg><h4>Dolorem eum fugiat quo voluptas nulla pariatur?</h4><p>Sed ut perspiciatis unde omnis iste natus error sit voluptatem accusantium doloremque laudantium, totam rem aperiam, eaque ipsa quae ab illo inventore veritatis et quasi architecto beatae vitae dicta sunt explicabo. Nemo enim ipsam voluptatem quia voluptas sit aspernatur aut odit aut</p></div>
  <div style="border-bottom:0"><svg width="22" height="22"><circle cx="11" cy="11" r="11" fill="#6b4fb5"/><path d="M6.5 11.3l3 3 6-6" stroke="#fff" fill="none" stroke-width="1.8"/></svg><h4>Dolorem eum fugiat quo voluptas nulla pariatur?</h4><p>Sed ut perspiciatis unde omnis iste natus error sit voluptatem accusantium doloremque laudantium, totam rem aperiam, eaque ipsa quae ab illo inventore veritatis et quasi architecto beatae vitae dicta sunt explicabo. Nemo enim ipsam voluptatem quia voluptas sit aspernatur aut odit aut</p></div>
  <div style="border:0"><svg width="22" height="22"><circle cx="11" cy="11" r="11" fill="#6b4fb5"/><path d="M6.5 11.3l3 3 6-6" stroke="#fff" fill="none" stroke-width="1.8"/></svg><h4>Dolorem eum fugiat quo voluptas nulla pariatur?</h4><p>Sed ut perspiciatis unde omnis iste natus error sit voluptatem accusantium doloremque laudantium, totam rem aperiam, eaque ipsa quae ab illo inventore veritatis et quasi architecto beatae vitae dicta sunt explicabo. Nemo enim ipsam voluptatem quia voluptas sit aspernatur aut odit aut</p></div>
</div>
<div class="photo" role="img" aria-label="Fashion doll in a sparkly pink dress" style="left:962px;top:3407px;width:124px;height:364px;border-radius:40px 40px 0 0;background:linear-gradient(#f1d69a,#e8bda0 35%,#cf5fa8 60%,#e9b89e)"></div>

<section class="abs fun">
  <div class="abs" style="left:63px;top:80px;width:340px">
    <h2><b>Fun</b> Zone</h2>
    <p style="font-size:12px;color:var(--muted);line-height:1.6;margin-top:18px">Sed ut perspiciatis unde omnis iste natus error sit voluptatem accusantium doloremque laudantium, totam rem aperiam, eaque ipsa quae ab illo inventore veritatis et quasi architecto</p>
  </div>
  <div class="photo" role="img" aria-label="Fashion doll with long blonde hair" style="left:500px;top:0;width:428px;height:488px;border-radius:0;background:linear-gradient(90deg,rgba(240,180,235,0),#efe0c8 30%,#e9cf9f 55%,#5fbfc9 80%,#ef9fe5)"></div>
</section>
<div class="tile" style="left:201px"><div class="ico" role="img" aria-label="Quiz badge illustration" style="background:linear-gradient(#f7c84a,#e59a2a)"></div><h4>Quizzes</h4><p>Duis aute irure dolor<br>in reprehenderit</p></div>
<div class="tile" style="left:356px"><div class="ico" role="img" aria-label="Mood faces illustration" style="background:linear-gradient(#ffb54a,#f1605e)"></div><h4>Mood Tracker</h4><p>Duis aute irure dolor<br>in reprehenderit</p></div>
<div class="tile" style="left:511px"><div class="ico" role="img" aria-label="Self-care figure illustration" style="background:linear-gradient(#f6a0b5,#8a63cf)"></div><h4>Self-Care Tips</h4><p>Duis aute irure dolor<br>in reprehenderit</p></div>

<footer class="abs footer">
  <h2 class="abs" style="left:0;width:1020px;top:70px;text-align:center;font-size:29px;font-weight:700">Sign Up For Our Newsletter</h2>
  <div class="abs" style="left:260px;top:132px;width:506px;height:38px;border-radius:19px;background:#e9eef8"></div>
  <span class="abs" style="left:283px;top:144px;font-size:10px;color:#333">Enter Your Email address</span>
  <div class="btn" style="left:651px;top:132px;width:115px;height:38px;border-radius:19px;font-size:10px;font-weight:700">SUBSCRIBE</div>
  <div class="abs" style="left:111px;top:220px;width:798px;height:1px;background:#3c3a40"></div>
  <span class="abs" style="left:111px;top:264px;font-size:11px;font-weight:700">CONTACT US</span>
  <span class="abs" style="left:228px;top:258px;width:24px;height:24px;border-radius:50%;background:var(--pink);display:flex;align-items:center;justify-content:center"><svg width="12" height="12" viewBox="0 0 24 24"><path d="M6 2l4 4-2 3c1 3 4 6 7 7l3-2 4 4-3 4C10 21 3 14 2 5z" fill="#222"/></svg></span>
  <span class="abs" style="left:262px;top:263px;font-size:10px">+1.555.0142.7788</span>
  <span class="abs" style="left:392px;top:258px;width:24px;height:24px;border-radius:50%;background:var(--pink);display:flex;align-items:center;justify-content:center"><svg width="12" height="10"><rect x=".5" y=".5" width="11" height="9" fill="none" stroke="#222"/><path d="M.5 .5l5.5 5 5.5-5" stroke="#222" fill="none"/></svg></span>
  <span class="abs" style="left:426px;top:263px;font-size:10px">hello@cyclewise.example</span>
  <div class="abs" style="left:741px;top:258px;display:flex;gap:8px">
    <span style="width:27px;height:27px;border-radius:50%;background:#fff"></span>
    <span style="width:27px;height:27px;border-radius:50%;background:#fff"></span>
    <span style="width:27px;height:27px;border-radius:50%;background:#fff"></span>
    <span style="width:27px;height:27px;border-radius:50%;background:#fff"></span>
    <span style="width:27px;height:27px;border-radius:50%;background:#fff"></span>
  </div>
  <div class="abs" style="left:111px;top:325px;width:798px;height:1px;background:#3c3a40"></div>
  <p class="abs" style="left:0;width:1020px;top:368px;text-align:center;font-size:11px;color:#ddd">Copyright © Cyclewise 2025. All rights reserved.</p>
</footer>
<div class="round" style="left:583px;top:4417px;background:#fff;border:1px solid #ddd"><svg width="14" height="16"><path d="M7 15V2M2 7l5-5 5 5" stroke="#222" fill="none" stroke-width="1.6"/></svg></div>
<div class="round" style="left:866px;top:4413px"><svg width="18" height="14"><rect x="1" y="1" width="16" height="12" rx="1" fill="none" stroke="#222" stroke-width="1.4"/><path d="M1 1l8 7 8-7" stroke="#222" fill="none" stroke-width="1.4"/></svg></div>
<div class="round" style="left:925px;top:4413px"><svg width="20" height="18"><path d="M2 2h16v10H8l-4 4v-4H2z" fill="#222"/></svg></div>
<div class="round" style="left:983px;top:4413px"><svg width="20" height="18"><path d="M3 12V9a7 7 0 0114 0v3" stroke="#222" fill="none" stroke-width="1.6"/><rect x="2" y="10" width="4" height="6" rx="1" fill="#222"/><rect x="14" y="10" width="4" height="6" rx="1" fill="#222"/></svg></div>

</body>
</html>
```